QM Studios needs and Interior Design Business card

I can do anything from Commercial to Residential and Free lance. Beginning to end in design selection process.
Need something to catch the eye of potential customers and vendors. From furniture to Tile and Cabinet selections. I can do it all.

Industry/Entity Type

Design Agency

Contact Information for Business Card

QM Studios- Design Consultanting Residential, Commerical
Maybe a cool detail background. Wall paper print that can have some texture

Font styles to use
Serif

Colors
709dcb
34a6d7
b868aa
e667a6
f59296
85acd3
ffffff
000000
5c5c5c

Requirements
Must have
• Square or Rectangular with Rounded edges
• Name
• Address
• Phone
• Email
Nice to have
• Some colored edges More simples not too busy
• Pattern detail in background.
Should not have
• Not too much color

```html
<!DOCTYPE html>
<html lang="en">
<head>
<meta charset="utf-8">
<title>QM Studios – Business Card</title>
<link href="https://fonts.googleapis.com/css2?family=Josefin+Sans:wght@300;400&family=Open+Sans:wght@400;700&display=swap" rel="stylesheet">
<style>
  :root {
    --stage: #2b2b2b;
    --sky: #2ea5d8;
    --blush: #f59296;
    --ink: #000000;
    --paper: #ffffff;
    --accent: #34a6d7;
  }
  * { margin: 0; padding: 0; box-sizing: border-box; }
  html, body { width: 1200px; height: 900px; overflow: hidden; background: var(--stage); }
  .canvas { position: relative; width: 1200px; height: 900px; }

  .card { position: absolute; width: 700px; height: 400px; overflow: hidden; box-shadow: 0 10px 30px rgba(0,0,0,.5); }

  /* Front */
  .card-front { left: 250px; top: 40px; background: var(--sky); }
  .front-mark { position: absolute; left: 250px; top: 100px; width: 200px; height: 200px;
    border: 6px solid var(--ink); border-radius: 50%;
    display: flex; align-items: center; justify-content: center; }
  .front-name { font-family: "Josefin Sans", sans-serif; font-weight: 300; font-size: 26px;
    letter-spacing: 3px; color: var(--ink); }

  /* Back */
  .card-back { left: 250px; top: 470px; background: var(--blush); }
  .brand-title { position: absolute; left: 150px; top: 90px; font-family: "Josefin Sans", sans-serif;
    font-weight: 300; font-size: 50px; letter-spacing: 12px; color: var(--ink); }
  .rule { position: absolute; left: 0; height: 3px; background: var(--paper); }
  .rule-top { top: 180px; width: 600px; }
  .rule-bottom { top: 350px; width: 700px; }
  .band { position: absolute; left: 0; top: 188px; width: 600px; height: 156px; background: var(--ink); }
  .band-mark { position: absolute; left: 525px; top: 105px; width: 160px; height: 160px; border-radius: 50%;
    background: var(--blush); border: 3px solid var(--paper); }
  .band-mark-inner { position: absolute; inset: 6px; border: 6px solid var(--ink); border-radius: 50%; }

  .contact { position: absolute; left: 36px; top: 205px; font-family: "Open Sans", sans-serif; color: var(--paper); }
  .contact-name { font-weight: 700; font-size: 24px; line-height: 1.1; }
  .contact-role { font-size: 14px; color: var(--accent); margin-bottom: 6px; letter-spacing: .5px; }
  .contact-line { font-size: 15px; line-height: 1.35; display: flex; align-items: center; gap: 8px; }
  .contact-line svg { width: 12px; height: 12px; flex: none; }
  .indent { padding-left: 20px; }
</style>
</head>
<body>
<main class="canvas">
  <section class="card card-front">
    <div class="front-mark"><span class="front-name">QM Studios</span></div>
  </section>

  <section class="card card-back">
    <h1 class="brand-title">QM Studios</h1>
    <div class="rule rule-top"></div>
    <div class="band"></div>
    <div class="rule rule-bottom"></div>
    <div class="band-mark"><div class="band-mark-inner"></div></div>

    <div class="contact">
      <p class="contact-name">DANA ROWE</p>
      <p class="contact-role">DIRECTOR</p>
      <p class="contact-line indent">Unit 2/8 Harbor Lane</p>
      <p class="contact-line indent">NORWOOD, QLD 4051</p>
      <p class="contact-line">
        <svg viewBox="0 0 24 24" aria-hidden="true"><path fill="#34a6d7" d="M6.6 10.8a15 15 0 0 0 6.6 6.6l2.2-2.2a1 1 0 0 1 1-.25 11.4 11.4 0 0 0 3.6.57 1 1 0 0 1 1 1V20a1 1 0 0 1-1 1A17 17 0 0 1 3 4a1 1 0 0 1 1-1h3.5a1 1 0 0 1 1 1c0 1.25.2 2.45.57 3.6a1 1 0 0 1-.25 1z"/></svg>
        +330 5512-7734
      </p>
      <p class="contact-line">
        <svg viewBox="0 0 24 24" aria-hidden="true"><rect x="2" y="5" width="20" height="14" fill="none" stroke="#34a6d7" stroke-width="2"/><path d="M2 6l10 7 10-7" fill="none" stroke="#34a6d7" stroke-width="2"/></svg>
        info@qmstudios.com
      </p>
    </div>
  </section>
</main>
</body>
</html>
```